Bramwick Client Journey To Success

I need a one-page document that graphically shows the client's journey working with Bramwick from initial assessment to completed project. I want the journey to start at the "basecamp logo" and reach 4 summits (little mountain logos...) .

I'd like the imagery to convey the client starting at basecamp, and moving to each summit. Each summit, should list the subtext under each, as listed on the pdf doc i provided.

The description for the basecamp and 4 summits is attached.

I need the brochure to look like the other brochure that you did for me (attached) .

Target Market(s)

Restaurant Owners

Industry/Entity Type

Construction Management

Font styles to use
Sans Serif

Colors
EB3D1F
EC4F4E
F09395
F8D3D4
FCEDEE

Requirements
Must have
• My logo. Title: Client Journey To Success. Subtitle: The 4 Summits

```html
<!DOCTYPE html>
<html lang="en">
<head>
<meta charset="utf-8">
<title>Bramwick – Client Journey, 4 Summits</title>
<link href="https://fonts.googleapis.com/css2?family=Montserrat:wght@500;600;700;800&family=Poppins:wght@400;500;700&display=swap" rel="stylesheet">
<style>
  :root {
    --red: #e3262b;
    --red-deep: #b9151c;
    --red-light: #ec4f4e;
    --charcoal: #2d3135;
    --ink: #2a2a2a;
    --rule: #8a8a8a;
    --paper: #ffffff;
    --backdrop: #2a2c2a;
  }
  * { box-sizing: border-box; margin: 0; padding: 0; }
  html, body { width: 1200px; height: 1199px; overflow: hidden; background: var(--backdrop); }
  .page {
    position: absolute; left: 193px; top: 25px;
    width: 754px; height: 1064px;
    background: var(--paper);
    transform: scale(1.08); transform-origin: top left;
    overflow: hidden;
    font-family: "Montserrat", sans-serif;
  }
  .header-visual { position: absolute; left: 0; top: 0; width: 754px; height: 268px; }
  .brand-tab { position: absolute; left: 303px; top: 0; width: 147px; height: 148px; }
  .brand-name {
    position: absolute; left: 303px; top: 96px; width: 147px;
    text-align: center; font-weight: 800; font-size: 9.5px; color: var(--ink);
    letter-spacing: 0.2px;
  }
  .brand-mark {
    position: absolute; left: 360px; top: 36px; width: 34px; height: 34px;
    background: var(--red);
  }
  .title {
    position: absolute; left: 248px; color: #fff; font-family: "Poppins", sans-serif;
  }
  .title-line { top: 158px; font-size: 35px; font-weight: 400; letter-spacing: 1px; }
  .title-main { top: 203px; font-size: 48px; font-weight: 700; line-height: 1; }

  .stage { position: absolute; width: 125px; height: 140px; }
  .stage svg { position: absolute; left: 0; top: 0; }
  .stage-label {
    position: absolute; left: 0; width: 125px; text-align: center; color: #fff;
    font-family: "Montserrat", sans-serif; font-weight: 800; line-height: 1.15;
  }
  .stage-label .big { font-size: 16px; display: block; }
  .stage-label .small { font-size: 11.5px; display: block; }
  .stage-num {
    position: absolute; left: 44px; top: -2px; width: 37px; height: 37px; border-radius: 50%;
    color: #fff; font-weight: 800; font-size: 21px; text-align: center; line-height: 37px;
  }
  .stage--red .stage-num { background: var(--charcoal); }
  .stage--dark .stage-num { background: var(--red); }

  .steps { position: absolute; list-style: none; }
  .steps li {
    height: 30px; line-height: 30px; font-size: 15px; font-weight: 500; color: var(--ink);
    border-bottom: 1px solid var(--rule); letter-spacing: 0.5px; white-space: nowrap;
  }
  .steps li:last-child { border-bottom: 1px solid var(--rule); }
  .steps .no-rule li:last-child { border-bottom: none; }
  .steps b { color: var(--red); font-weight: 700; margin-right: 4px; }
  .photo { position: absolute; }
</style>
</head>
<body>
<main class="page">
  <svg class="header-visual" viewBox="0 0 754 268" role="img" aria-label="Photo of glass skyscrapers seen from below at sunset">
    <defs>
      <linearGradient id="sky" x1="0" y1="0" x2="1" y2="0">
        <stop offset="0" stop-color="#3c3f42"/>
        <stop offset="0.35" stop-color="#8d9196"/>
        <stop offset="0.6" stop-color="#c9c1b6"/>
        <stop offset="0.85" stop-color="#d98a4a"/>
        <stop offset="1" stop-color="#7a4028"/>
      </linearGradient>
    </defs>
    <rect width="754" height="268" fill="url(#sky)"/>
    <path d="M200 148 H620 a12 12 0 0 1 12 12 V205 H200 Z" fill="#1d1f22" opacity="0.55"/>
    <rect x="200" y="205" width="554" height="61" fill="var(--red-deep)" opacity="0.9"/>
    <rect x="0" y="266" width="754" height="2" fill="var(--red)"/>
  </svg>

  <svg class="brand-tab" viewBox="0 0 147 148" aria-hidden="true">
    <path d="M0 0 H147 V118 Q147 128 137 132 L80 146 Q73 148 66 146 L10 132 Q0 128 0 118 Z" fill="#fff"/>
  </svg>
  <div class="brand-mark" aria-hidden="true"></div>
  <div class="brand-name">BRAMWICK DEVELOPMENT</div>

  <div class="title title-line">Client Journey</div>
  <div class="title title-main">4 Summits</div>

  <!-- Stage 1 -->
  <div class="stage stage--red" style="left:26px; top:280px;">
    <svg width="125" height="140" viewBox="0 0 125 140"><defs><linearGradient id="redHex" x1="0" y1="0" x2="0" y2="1"><stop offset="0" stop-color="#ec3b2e"/><stop offset="1" stop-color="#c4161c"/></linearGradient></defs><polygon points="62.5,0 125,35 125,105 62.5,140 0,105 0,35" fill="url(#redHex)"/></svg>
    <div class="stage-num">1.</div>
    <div class="stage-label" style="top:61px;"><span class="big">Basecamp</span></div>
  </div>
  <ul class="steps" style="left:162px; top:300px; width:222px;">
    <li><b>a.</b>Client Assessment</li>
    <li><b>b.</b>Determine Project Goals</li>
    <li><b>c.</b>Proposal &amp; Fees</li>
  </ul>

  <!-- Stage 2 -->
  <div class="stage stage--dark" style="left:26px; top:443px;">
    <svg width="125" height="140" viewBox="0 0 125 140"><polygon points="62.5,0 125,35 125,105 62.5,140 0,105 0,35" fill="var(--charcoal)"/></svg>
    <div class="stage-num">2.</div>
    <div class="stage-label" style="top:60px;"><span class="big">Summit 1 -</span><span class="small">PreConstruction</span></div>
  </div>
  <ul class="steps" style="left:162px; top:418px; width:294px;">
    <li><b>a.</b>Develop Project Plan</li>
    <li><b>b.</b>Develop Risk Assessment &amp; Plan</li>
    <li><b>c.</b>Devlelop Schedule</li>
    <li><b>d.</b>Develop Budget</li>
    <li><b>e.</b>Develop Team</li>
    <li style="border-bottom:none;"><b>f.</b>GC, Sub, Consultants Contracts</li>
  </ul>

  <svg class="photo" style="left:405px; top:290px;" width="330" height="308" viewBox="0 0 330 308" role="img" aria-label="Photo of a winding mountain road at sunrise">
    <defs><linearGradient id="hill" x1="1" y1="0" x2="0" y2="1"><stop offset="0" stop-color="#f4c774"/><stop offset="0.35" stop-color="#b8893e"/><stop offset="0.7" stop-color="#5d6b2c"/><stop offset="1" stop-color="#36421f"/></linearGradient></defs>
    <path d="M20 2 H300 a30 30 0 0 1 30 30 V276 a30 30 0 0 1 -30 30 H135 a30 30 0 0 1 -28 -20 L2 30 Q-4 2 20 2 Z" fill="url(#hill)"/>
  </svg>

  <svg class="photo" style="left:26px; top:605px;" width="252" height="438" viewBox="0 0 252 438" role="img" aria-label="Photo of tower cranes over a building construction site">
    <defs><linearGradient id="site" x1="0" y1="0" x2="0" y2="1"><stop offset="0" stop-color="#cfdde6"/><stop offset="0.55" stop-color="#e7dccb"/><stop offset="0.8" stop-color="#8b7f66"/><stop offset="1" stop-color="#4c4a3e"/></linearGradient></defs>
    <path d="M26 0 H110 Q126 0 140 10 L238 92 Q252 104 252 120 V414 a24 24 0 0 1 -24 24 H24 a24 24 0 0 1 -24 -24 V26 A26 26 0 0 1 26 0 Z" fill="url(#site)"/>
  </svg>

  <!-- Stage 3 -->
  <div class="stage stage--red" style="left:300px; top:613px;">
    <svg width="125" height="140" viewBox="0 0 125 140"><polygon points="62.5,0 125,35 125,105 62.5,140 0,105 0,35" fill="url(#redHex)"/></svg>
    <div class="stage-num">3.</div>
    <div class="stage-label" style="top:56px;"><span class="big">Summit 1 -</span><span class="small">PreConstruction</span></div>
  </div>
  <ul class="steps" style="left:440px; top:635px; width:232px;">
    <li><b>a.</b>Acquire Permits</li>
    <li><b>b.</b>PreConstruction Meeting</li>
    <li><b>c.</b>Project Start</li>
  </ul>

  <!-- Stage 4 -->
  <div class="stage stage--dark" style="left:300px; top:765px;">
    <svg width="125" height="140" viewBox="0 0 125 140"><polygon points="62.5,0 125,35 125,105 62.5,140 0,105 0,35" fill="var(--charcoal)"/></svg>
    <div class="stage-num">4.</div>
    <div class="stage-label" style="top:44px;"><span class="big" style="font-size:15px;">Summit 3 -</span><span class="big" style="font-size:14px;">Project</span><span class="big" style="font-size:14px;">Management</span></div>
  </div>
  <ul class="steps" style="left:440px; top:771px; width:284px;">
    <li><b>a.</b>Shared Consciousness Meetings</li>
    <li><b>b.</b>Pressurized Collaboration</li>
    <li><b>c.</b>Schedule Management</li>
    <li><b>d.</b>Run O.O.D.A. Loop</li>
  </ul>

  <!-- Stage 5 -->
  <div class="stage stage--red" style="left:300px; top:916px;">
    <svg width="125" height="140" viewBox="0 0 125 140"><polygon points="62.5,0 125,35 125,105 62.5,140 0,105 0,35" fill="url(#redHex)"/></svg>
    <div class="stage-num">4.</div>
    <div class="stage-label" style="top:44px;"><span class="big" style="font-size:15px;">Summit 3 -</span><span class="big" style="font-size:14px;">Project</span><span class="big" style="font-size:14px;">Management</span></div>
  </div>
  <ul class="steps" style="left:440px; top:970px; width:286px;">
    <li><b>a.</b>Closeout</li>
  </ul>
</main>
</body>
</html>
```